Lumora Terrain services flyer

We are looking for some eye-catching flyer designs templates for our company lumora terrain pages. We are open to any designs but prefer the theme colour to be similar to our logo colours or something goes well with the colours.
We have attached a pptx that has texts and figures we would like to put on the flyer, please combined slide 1&2 as front page and 3-5 as back page.
Requirements:
Colour theme: similar to logo colours or something that goes well with it (logo is attached)
Page: two sides A4 size
Text & front: No specific requirements
Reference/examples:
- Below website demonstrates how we use our machines for those applications
http://www.brindlecove.example/applications_home.html
- Same applies to slide 11 - 25 from link below
http://www.marcuvelten.example.au/public/documents/5/18/Layered%20Survey%20of%20Bronze%20Ridge%20Basins.pdf

```html
<!DOCTYPE html>
<html lang="en">
<head>
<meta charset="utf-8">
<title>Lumora Terrain Training Flyer</title>
<link href="https://fonts.googleapis.com/css2?family=Open+Sans:ital,wght@0,400;0,700;1,700&display=swap" rel="stylesheet">
<style>
  :root {
    --orange: #ee8631;
    --white: #ffffff;
    --page-bg: #ecebe8;
    --red: #e3141b;
    --photo-light: #eef1f3;
    --photo-mid: #c9c3b6;
    --photo-blue: #3c6f9e;
    --fig-dark: #0c0c0c;
    --fig-sheet: #ecebe6;
    --model-warm: #d9793a;
    --model-cool: #9cbf6e;
  }
  * { margin: 0; padding: 0; box-sizing: border-box; }
  html, body { width: 1200px; height: 1200px; overflow: hidden; }
  body { background: var(--page-bg); font-family: "Open Sans", sans-serif; }

  .flyer {
    position: absolute; left: 197px; top: 30px;
    width: 806px; height: 1140px;
    background: var(--white); overflow: hidden;
    box-shadow: 0 4px 14px rgba(0,0,0,.18);
  }
  .photo-field {
    position: absolute; left: 0; top: 640px; width: 806px; height: 500px;
    background: linear-gradient(180deg, var(--white) 0%, var(--photo-light) 15%, var(--photo-mid) 50%, #a98a5c 72%, var(--photo-blue) 100%);
  }
  .info-panel {
    position: absolute; left: 0; top: 0; width: 374px; height: 1017px;
    background: var(--orange); color: var(--white);
    padding: 47px 40px 0 45px;
    font-size: 16.2px; line-height: 22.2px;
  }
  .info-panel .lead { font-weight: 700; margin-bottom: 22px; }
  .info-panel p { margin-bottom: 22px; }
  .info-panel .contact { font-weight: 700; font-style: italic; }

  .figure { position: absolute; }
  .fig-striplog { left: 427px; top: 50px; width: 186px; height: 135px; background: var(--fig-dark); }
  .fig-alteration { background: linear-gradient(180deg, var(--fig-sheet) 30%, #f2d488 55%, #6fa9d8 85%); border: 2px solid #333; }
  .fig-alteration-a { left: 590px; top: 101px; width: 170px; height: 120px; }
  .fig-alteration-b { left: 408px; top: 247px; width: 198px; height: 139px; }
  .fig-map { left: 537px; top: 335px; width: 224px; height: 147px; background: linear-gradient(135deg, #e6e6e6, #a8a8a8 60%, #d8d8d8); border: 1px solid #bbb; }
  .fig-model { left: 446px; top: 485px; width: 286px; height: 210px;
    background: linear-gradient(160deg, var(--model-warm) 0%, var(--model-cool) 100%); }

  .target-callout { position: absolute; left: 403px; top: 188px; }

  .brand {
    position: absolute; left: 430px; top: 1040px;
    display: flex; align-items: center; gap: 10px; white-space: nowrap;
    color: var(--orange); font-weight: 700; font-size: 20px; letter-spacing: .5px;
  }
  .brand-dot { width: 36px; height: 36px; border-radius: 50%; background: var(--orange); }
</style>
</head>
<body>
  <main class="flyer">
    <div class="photo-field" role="img" aria-label="Photograph of a geologist in a white hard hat and blue shirt looking up at an open-pit mine"></div>

    <section class="info-panel">
      <p class="lead">Halvern Ridge Exploration provides a complete LUMORA TERRAIN TRAINING service.</p>
      <p>Courses on equipment use, licencing and data interpretation are available to early career geoscientists, senior geologists and exploration managers across Asia, Africa, Australia, Canada, Europe, Pacific Rim Nations and South America.</p>
      <p>Learn how KLS / TRV specialists acquire and validate spectral data from soil, rock chip and downhole samples (chips and core).</p>
      <p>Understand how Lumora Terrain geologists interpret KLS / TRV strip logs, develop alteration models and identify mineralisation vectors.</p>
      <p>Meet senior geologists that integrate spectral data with drilling, false-colour imagery (satellite data), lithology, geochemical assays, geochronology, geophysics, radiometrics and structure to generate high-quality exploration targets.</p>
      <p>Participate in a case-study where generative consultants integrate alteration models and mineralisation vectors with field mapping, mineral distribution intensity and abundance maps, grade shell models, geophysics and tectonic models to produce new exploration concepts.</p>
      <p class="contact">Call or Email Halvern Ridge Exploration<br>+61 7 3000 41 27</p>
    </section>

    <div class="figure fig-striplog" role="img" aria-label="Spectral strip log chart with coloured mineral bands on black"></div>
    <div class="figure fig-alteration fig-alteration-a" role="img" aria-label="Alteration cross-section diagram with new target points"></div>
    <svg class="target-callout" width="186" height="24" viewBox="0 0 186 24" aria-label="New Targets">
      <circle cx="9" cy="11" r="9" fill="var(--red)"/>
      <text x="27" y="17" font-family="Open Sans, sans-serif" font-weight="700" font-size="16" fill="var(--red)">New Targets</text>
      <line x1="134" y1="12" x2="175" y2="12" stroke="var(--red)" stroke-width="4"/>
      <polygon points="175,6 184,12 175,18" fill="var(--red)"/>
    </svg>
    <div class="figure fig-alteration fig-alteration-b" role="img" aria-label="Alteration cross-section diagram"></div>
    <div class="figure fig-map" role="img" aria-label="Plan map of mined shoots with a new discovery marked"></div>
    <div class="figure fig-model" role="img" aria-label="3D grade shell block model with drill holes"></div>

    <div class="brand"><span class="brand-dot"></span><span>HALVERN RIDGE EXPLORATION</span></div>
  </main>
</body>
</html>
```